Walking Faithful Pathways book cover design

Title: Walking Faithful Pathways
Subtitle: How to hear and do the will of God

Ed Brantwell

top of book starburst or graphic: Updated & Expanded!

Design front, back cover and spine

Size: 8 1/2 inches x 5 1/2 inches, color, spine 1/4 inch

Book is about helping Christian understand how to hear God and how to make Godly decisions in life and work.

Target Market(s)

Christian evangelical audience, men and women adults

Colors

Designer to choose colors to be used in the design.

Requirements
Must have
• Open to suggestions
Nice to have
• Open to suggestions

```html
<!DOCTYPE html>
<html lang="en">
<head>
<meta charset="utf-8">
<title>Walking Faithful Pathways — Cover Spread</title>
<link rel="stylesheet" href="https://fonts.googleapis.com/css2?family=Smokum&family=Stint+Ultra+Condensed&family=Dosis:wght@400;500&family=Parisienne&display=swap">
<style>
  :root {
    --stage: #7b7b7b;
    --ink-blue: #1f4584;
    --badge-blue: #3f8fd0;
    --badge-ring: #ffffff;
    --sky-top: #a9c6e6;
    --sky-mid: #d4e3f3;
    --mist: #f4f7fb;
    --script-blue: #3a78c2;
    --spine: #eef2f7;
    --small-ink: #5a6a80;
  }
  html, body {
    margin: 0;
    width: 1200px;
    height: 1000px;
    overflow: hidden;
    background: var(--stage);
  }
  .spread {
    position: absolute;
    left: 37px;
    top: 75px;
    width: 1125px;
    height: 850px;
    display: flex;
  }
  .back-cover, .front-cover {
    position: relative;
    width: 550px;
    height: 850px;
    overflow: hidden;
    background: var(--mist);
  }
  .spine {
    width: 25px;
    height: 850px;
    background: var(--spine);
  }
  .back-photo {
    position: absolute;
    inset: 0;
    background:
      radial-gradient(ellipse 120px 200px at 420px 380px, rgba(170,190,215,0.55), rgba(170,190,215,0) 70%),
      linear-gradient(180deg, #9fbde2 0%, #c9dbef 35%, #e3ecf6 60%, var(--mist) 100%);
  }
  .front-photo {
    position: absolute;
    inset: 0;
    background:
      radial-gradient(ellipse 130px 120px at 270px 300px, rgba(255,255,255,0.95), rgba(255,255,255,0) 70%),
      linear-gradient(180deg, var(--sky-top) 0%, var(--sky-mid) 35%, #e6eef7 60%, var(--mist) 100%);
  }
  .copyright {
    position: absolute;
    left: 70px;
    top: 670px;
    width: 240px;
    margin: 0;
    font-family: "Dosis", sans-serif;
    font-size: 10.5px;
    line-height: 1.35;
    color: var(--small-ink);
  }
  .author {
    position: absolute;
    left: 110px;
    top: 52px;
    width: 240px;
    text-align: center;
    white-space: nowrap;
    font-family: "Dosis", sans-serif;
    font-weight: 500;
    font-size: 24px;
    letter-spacing: 5px;
    color: var(--ink-blue);
  }
  .badge {
    position: absolute;
    left: 380px;
    top: 40px;
    width: 124px;
    height: 124px;
  }
  .badge-label {
    font-family: "Dosis", sans-serif;
    font-weight: 500;
    font-size: 15px;
    letter-spacing: 1px;
    fill: #fff;
  }
  .title {
    position: absolute;
    left: 0;
    top: 260px;
    width: 550px;
    height: 400px;
    margin: 0;
  }
  .title-line {
    font-family: "Smokum", "Stint Ultra Condensed", serif;
    font-size: 128px;
    fill: var(--ink-blue);
  }
  .divider {
    position: absolute;
    left: 75px;
    top: 682px;
    width: 400px;
    height: 16px;
  }
  .subtitle {
    position: absolute;
    left: 0;
    top: 705px;
    width: 100%;
    margin: 0;
    text-align: center;
    white-space: nowrap;
    font-family: "Parisienne", cursive;
    font-size: 26px;
    color: var(--script-blue);
  }
</style>
</head>
<body>
  <div class="spread">
    <section class="back-cover">
      <div class="back-photo" role="img" aria-label="Soft sky and misty sea with a faint reflection of the seated figure"></div>
      <p class="copyright">© Ed Brantwell, 2019. All Rights Reserved. Unauthorized reproduction, use, or sharing, in part or in whole, is strictly prohibited.</p>
    </section>

    <div class="spine"></div>

    <main class="front-cover">
      <div class="front-photo" role="img" aria-label="Bright sky and misty sea with a man seated in meditation on a rock, sun glowing behind him"></div>

      <div class="author">ED BRANTWELL</div>

      <svg class="badge" viewBox="0 0 124 124" aria-label="Updated and Expanded!">
        <g fill="var(--badge-blue)">
          <rect x="20" y="20" width="84" height="84" transform="rotate(0 62 62)"/>
          <rect x="20" y="20" width="84" height="84" transform="rotate(15 62 62)"/>
          <rect x="20" y="20" width="84" height="84" transform="rotate(30 62 62)"/>
          <rect x="20" y="20" width="84" height="84" transform="rotate(45 62 62)"/>
          <rect x="20" y="20" width="84" height="84" transform="rotate(60 62 62)"/>
          <rect x="20" y="20" width="84" height="84" transform="rotate(75 62 62)"/>
        </g>
        <circle cx="62" cy="62" r="48" fill="none" stroke="var(--badge-ring)" stroke-width="1.5"/>
        <g transform="rotate(-8 62 62)">
          <text class="badge-label" x="62" y="58" text-anchor="middle">UPDATED &amp;</text>
          <text class="badge-label" x="62" y="78" text-anchor="middle">EXPANDED!</text>
        </g>
      </svg>

      <h1 class="title">
        <svg viewBox="0 0 550 400" width="550" height="400">
          <text class="title-line" x="275" y="118" text-anchor="middle" textLength="360" lengthAdjust="spacingAndGlyphs">WALKING</text>
          <text class="title-line" x="275" y="250" text-anchor="middle" textLength="380" lengthAdjust="spacingAndGlyphs">FAITHFUL</text>
          <text class="title-line" x="275" y="382" text-anchor="middle" textLength="400" lengthAdjust="spacingAndGlyphs">PATHWAYS</text>
        </svg>
      </h1>

      <svg class="divider" viewBox="0 0 400 16" aria-hidden="true">
        <path d="M4 8 L14 4 L14 12 Z" fill="var(--script-blue)"/>
        <line x1="24" y1="8" x2="376" y2="8" stroke="var(--script-blue)" stroke-width="2" stroke-dasharray="2 6"/>
        <path d="M396 8 L386 4 L386 12 Z" fill="var(--script-blue)"/>
      </svg>

      <p class="subtitle">How to hear and do the will of God</p>
    </main>
  </div>
</body>
</html>
```